Business Card Design For A Renovation Contractor Company

We need a business card for a new company based in Singapore, our company name is "KT Planora". We are a renovation contractor that builds designs into reality. We build more of F&B restaurants, retail stores and commercial offices. We work very closely with designers. The final design should communicate to our client that we are a company that you can trust, that will plan and complete your project without giving you a headache. I like my client to remember my company as "KT". The beauty of SIMPLE is important.

Industry/Entity Type

Contractor

Requirements
Nice to have
• Black or Red base

```html
<!DOCTYPE html>
<html lang="en">
<head>
<meta charset="utf-8">
<title>KT Planora — Business Card</title>
<link rel="stylesheet" href="https://fonts.googleapis.com/css2?family=Questrial&family=Open+Sans:wght@400&display=swap">
<style>
  :root {
    --stage: #2b2b2d;
    --card: #050505;
    --card-edge: #1a1a1a;
    --white: #f4f4f4;
    --red: #e0161d;
    --smoke: #8a8a8a;
  }
  * { box-sizing: border-box; margin: 0; padding: 0; }
  html, body { width: 1200px; height: 800px; overflow: hidden; }
  body {
    background: var(--stage);
    display: flex;
    align-items: center;
    justify-content: center;
    gap: 40px;
  }
  .card {
    position: relative;
    width: 540px;
    height: 309px;
    background: radial-gradient(ellipse at 40% 30%, #151515 0%, var(--card) 70%);
    border: 1px solid var(--card-edge);
    overflow: hidden;
  }

  /* Front */
  .name-row {
    position: absolute;
    left: 52px;
    right: 0;
    top: 58px;
    display: flex;
    align-items: center;
    gap: 14px;
  }
  .wordmark {
    font-family: "Questrial", sans-serif;
    font-size: 62px;
    line-height: 1;
    color: var(--white);
    letter-spacing: -1px;
    white-space: nowrap;
  }
  .accent-rule {
    flex: 1;
    height: 3px;
    margin-top: 8px;
    background: var(--red);
  }
  .base-rule {
    position: absolute;
    left: 0;
    width: 440px;
    top: 132px;
    height: 2px;
    background: var(--white);
  }
  .tagline {
    position: absolute;
    left: 64px;
    top: 137px;
    font-family: "Questrial", sans-serif;
    font-size: 22px;
    line-height: 1.1;
    color: var(--white);
    letter-spacing: 0.3px;
    white-space: nowrap;
  }
  .smoke-area {
    position: absolute;
    left: 120px;
    top: 170px;
    width: 300px;
    height: 105px;
    border-radius: 50%;
    background: radial-gradient(ellipse at center, rgba(138,138,138,0.35) 0%, rgba(138,138,138,0.12) 45%, rgba(0,0,0,0) 72%);
  }
  .phone {
    position: absolute;
    left: 0;
    right: 0;
    bottom: 34px;
    text-align: center;
    font-family: "Open Sans", sans-serif;
    font-size: 16px;
    letter-spacing: 1.5px;
    color: var(--white);
  }

  /* Back */
  .card-back {
    display: flex;
    align-items: center;
    justify-content: center;
    gap: 14px;
  }
  .mark-dot {
    width: 22px;
    height: 22px;
    border-radius: 50%;
    background: var(--red);
  }
  .back-name {
    font-family: "Questrial", sans-serif;
    font-size: 40px;
    color: var(--red);
    letter-spacing: -0.5px;
  }
</style>
</head>
<body>
  <section class="card card-front">
    <div class="name-row">
      <div class="wordmark">KT Planora</div>
      <div class="accent-rule"></div>
    </div>
    <div class="base-rule"></div>
    <p class="tagline">every space built to the plan</p>
    <div class="smoke-area" role="img" aria-label="Soft wisp of white smoke curling across the card"></div>
    <p class="phone">081-555-246</p>
  </section>

  <section class="card card-back">
    <span class="mark-dot"></span>
    <span class="back-name">KT Planora</span>
  </section>
</body>
</html>
```